Brochure Design

I would like to have this brochure design for a approval with the Morvale chamber of commerce . It's a training program for people in Kenya Africa and the gov will pay for the training program. What ever you think would be better let me know. The letters in red are items that are free so I wanted that to stand out. I need to add the logo in the attachment added to the other logos on the front page.

Reason: I'm still looking for the right design and i'm looking to make a quick decision.

```html
<!DOCTYPE html>
<html lang="en">
<head>
<meta charset="utf-8">
<title>Meridian Mobility Enterprises – Training Program Outline</title>
<link rel="stylesheet" href="https://fonts.googleapis.com/css2?family=Cinzel:wght@400;700&family=PT+Sans:wght@400;700&display=swap">
<style>
  :root {
    --stage-light: #6a6c6e;
    --stage-dark: #2a2b2c;
    --band: #2c2f32;
    --page: #f4f5f5;
    --gold: #c9a24a;
    --ink: #111111;
    --body-ink: #1e1e1e;
    --white: #ffffff;
    --frame: #3a3d40;
  }
  * { box-sizing: border-box; margin: 0; padding: 0; }
  html, body { width: 1200px; height: 999px; overflow: hidden; }
  body {
    position: relative;
    background: radial-gradient(ellipse at 50% 40%, var(--stage-light) 0%, #4a4c4e 45%, var(--stage-dark) 100%);
    font-family: "PT Sans", Arial, sans-serif;
  }
  .spread-label {
    position: absolute; top: 38px;
    font-family: "Cinzel", "Times New Roman", serif;
    font-weight: 700; font-size: 78px; color: var(--ink);
    line-height: 1; text-align: center; width: 542px;
  }
  .spread-label--cover { left: 46px; }
  .spread-label--inner { left: 636px; }

  .page {
    position: absolute; top: 175px; width: 542px; height: 702px;
    background: var(--page); overflow: hidden;
    box-shadow: 0 0 0 1px rgba(0,0,0,.35);
  }
  .page--cover { left: 46px; }
  .page--inner { left: 636px; }

  .brand {
    display: flex; align-items: center; gap: 10px;
    color: var(--gold); font-family: "PT Sans", Arial, sans-serif; font-weight: 400;
  }
  .brand__dot { border-radius: 50%; border: 3px solid var(--gold); }

  /* Cover */
  .cover__header {
    height: 123px; background: var(--band);
    display: flex; justify-content: center; align-items: center;
  }
  .cover__header .brand { font-size: 24px; }
  .cover__header .brand__dot { width: 58px; height: 58px; }
  .cover__photo {
    position: absolute; top: 123px; left: 0; width: 542px; height: 364px;
    background: linear-gradient(180deg, #1b3c6b 0%, #5f8fc7 38%, #2a5690 62%, #0c1f3d 78%, #3e6ea8 100%);
  }
  .cover__title {
    position: absolute; left: 24px; top: 396px;
    font-family: "Cinzel", "Times New Roman", serif; font-weight: 700;
    font-size: 30px; line-height: 38px; color: var(--white);
    text-shadow: 2px 2px 3px rgba(0,0,0,.8);
  }
  .cover__inset {
    position: absolute; left: 342px; top: 405px; width: 173px; height: 150px;
    border: 6px solid var(--frame);
    background: linear-gradient(180deg, #3c4f6e 0%, #c7d0da 45%, #8b8f93 75%, #5b5e61 100%);
  }
  .cover__partners-intro {
    position: absolute; left: 24px; top: 508px;
    font-size: 24px; line-height: 31px; color: var(--body-ink);
  }
  .cover__partners {
    position: absolute; left: 12px; top: 600px; width: 520px; height: 48px;
    display: flex; align-items: center; gap: 10px;
  }
  .partner-badge { height: 44px; }
  .partner-badge--wide { width: 118px; background: #e7e9ec; }
  .partner-badge--square { width: 44px; background: #e8d623; }
  .partner-badge--mid { width: 68px; background: #d9e7d6; }
  .partner-badge--chamber { width: 90px; background: #e4e4e6; }
  .partner-badge--note { width: 120px; margin-left: auto; background: #f0e3e3; height: 30px; }

  .page__footer {
    position: absolute; left: 0; bottom: 0; width: 542px; height: 42px;
    background: var(--band); color: var(--white);
    display: flex; align-items: center; justify-content: center; font-size: 17px;
  }
  .page__number { position: absolute; left: 12px; font-size: 10px; }

  /* Inner */
  .inner__header {
    height: 42px; background: var(--band);
    display: flex; justify-content: flex-end; align-items: center; padding-right: 16px;
  }
  .inner__header .brand { font-size: 11px; gap: 5px; }
  .inner__header .brand__dot { width: 22px; height: 22px; border-width: 2px; }
  .overview__title {
    margin-top: 12px; text-align: center;
    font-family: "Cinzel", "Times New Roman", serif; font-weight: 700;
    font-size: 30px; color: var(--ink);
  }
  .overview__body { padding: 14px 20px 0 22px; }
  .overview__body p {
    font-size: 10.6px; line-height: 14.4px; color: var(--body-ink);
    text-align: justify; margin-bottom: 14px;
  }
  .overview__figure {
    position: absolute; left: 101px; top: 428px; width: 340px; height: 228px;
    background: var(--white); padding: 4px;
    box-shadow: 0 1px 4px rgba(0,0,0,.45);
  }
  .overview__figure-fill {
    width: 100%; height: 100%;
    background: radial-gradient(ellipse at 55% 50%, #3f6fd0 0%, #17347f 55%, #0a1440 100%);
  }
</style>
</head>
<body>
  <div class="spread-label spread-label--cover">Cover</div>
  <div class="spread-label spread-label--inner">Inner</div>

  <section class="page page--cover">
    <header class="cover__header">
      <div class="brand"><span class="brand__dot"></span><span>Meridian Mobility Enterprises</span></div>
    </header>
    <div class="cover__photo" role="img" aria-label="City skyline at night reflected on water, in cool blue light"></div>
    <h1 class="cover__title">Training<br>Program Outline</h1>
    <div class="cover__inset" role="img" aria-label="Passenger airplane on a runway under a cloudy sky"></div>
    <p class="cover__partners-intro">In Conjunction With<br>Velnora and</p>
    <div class="cover__partners" aria-label="Partner organisations, including the Morvale chamber of commerce">
      <span class="partner-badge partner-badge--wide"></span>
      <span class="partner-badge partner-badge--square"></span>
      <span class="partner-badge partner-badge--mid"></span>
      <span class="partner-badge partner-badge--chamber"></span>
      <span class="partner-badge partner-badge--note"></span>
    </div>
    <footer class="page__footer">www.meridianmobilityenterprises.com</footer>
  </section>

  <section class="page page--inner">
    <header class="inner__header">
      <div class="brand"><span class="brand__dot"></span><span>Meridian Mobility Enterprises</span></div>
    </header>
    <h2 class="overview__title">OVERVIEW</h2>
    <div class="overview__body">
      <p>Meridian Mobility Enterprises is an American corporation that is dedicated to fostering cross cultural learning and experiences for the purpose of bettering people in all areas of the world.</p>
      <p>Our goal is to give African people training in fields that will improve daily life and give them business opportunities. It will open up opportunities to be able to better feed their families, live in safer, easier to build, affordable homes, and earn a living so that they can be proud of themselves and their ability to support their family.</p>
      <p>In addition to training programs in Africa, we have several different areas of practice, including working with investors who want to open a company in the United States, and helping them to navigate the detailed business processes in order operate successful businesses.</p>
      <p>We also have a sister company, Crossroads Cultural Exchange Institute, which has U.S. Department of State approval to administer internship programs in the United States for foreign students who are enrolled in college, university or other post-secondary education and desire to increase their skills, knowledge, and education by having experiences in America. This organization also assists with visa processing for all of our clients.</p>
      <p>All of the training programs you will read about in this manual are taught in Nairobi, Kenya, with the exception of the Commercial Fish Farming program which is taught in the United States.</p>
    </div>
    <figure class="overview__figure">
      <div class="overview__figure-fill" role="img" aria-label="Glowing world map with connection lines between continents"></div>
    </figure>
    <footer class="page__footer"><span class="page__number">01</span>www.meridianmobilityenterprises.com</footer>
  </section>
</body>
</html>
```